Business card and stationery for startup company
Marla Quenby & Associates
Business card and stationery for startup company - Corporate Services
Creative Brief
Professional
Marla Quenby
PO Box 382 Northville, MI 48193
marlaequenby@postvane.com
Concepts
Business Cards and Stationery for Background Check Company
Business Cards and Stationery for new compliance company.

```html
<!DOCTYPE html>
<html lang="en">
<head>
<meta charset="utf-8">
<title>Marla Quenby &amp; Associates — Stationery Set</title>
<link rel="stylesheet" href="https://fonts.googleapis.com/css2?family=Cinzel:wght@600&family=Open+Sans:wght@400;600&display=swap">
<style>
  :root{
    --bg:#e8e5e0;
    --paper:#ffffff;
    --navy:#1b3f7a;
    --blue:#2467b3;
    --blue-light:#4f8fd6;
    --brown:#6a3a20;
    --brown-light:#8f5635;
    --grey:#8a8f96;
    --line:#b9bec6;
    --swirl:#dfe4ea;
  }
  *{box-sizing:border-box;margin:0;padding:0}
  html,body{width:1200px;height:665px;overflow:hidden;background:var(--bg)}
  body{position:relative;font-family:"Open Sans",Arial,sans-serif;color:var(--navy)}
  .caption{position:absolute;font-size:5px;color:#555;text-align:center;letter-spacing:.2px}
  .sheet{position:absolute;background:var(--paper);box-shadow:0 1px 4px rgba(0,0,0,.25);overflow:hidden}
  .brand{display:flex;align-items:center;gap:5px}
  .brand-dot{border-radius:50%;background:var(--blue);flex:none}
  .brand-name{font-family:"Cinzel",Georgia,serif;font-weight:600;color:var(--navy);white-space:nowrap}
  .brand-tag{font-size:4px;color:var(--grey);letter-spacing:.3px;white-space:nowrap;margin-top:1px}
  .pattern{position:absolute;border-radius:50%;background:radial-gradient(ellipse at 60% 40%,var(--swirl),rgba(223,228,234,0) 70%)}
  .wave{position:absolute;left:0;bottom:0;width:100%}
  .footer-text{position:absolute;left:0;right:0;bottom:5px;text-align:center;font-size:5px;color:#fff;letter-spacing:.3px}
  /* business cards */
  .card{width:95px;height:52px;top:16px}
  .card-blue{background:linear-gradient(160deg,var(--blue-light),var(--navy))}
  .card-brown{background:linear-gradient(160deg,var(--brown-light),var(--brown))}
  .card .brand-name{font-size:4.6px}
  .card-back .brand-name{color:#fff}
  .card-back .brand{position:absolute;left:10px;top:20px}
  .card-front .brand{position:absolute;left:6px;top:9px}
  .card-contact{position:absolute;left:8px;top:30px;font-size:3.4px;line-height:5px;color:var(--navy)}
  /* fax */
  .fax-title{position:absolute;right:18px;top:58px;font-size:6px;font-weight:600}
  .fax-table{position:absolute;left:18px;top:66px;width:200px;border-collapse:collapse;font-size:4.5px}
  .fax-table td{border:1px solid var(--line);height:11px;padding:0 3px;color:var(--navy)}
  .fax-table td.lbl{width:22px}
  .fax-checks{position:absolute;left:18px;top:130px;display:flex;gap:14px;font-size:4.5px}
  .fax-checks span::before{content:"";display:inline-block;width:4px;height:4px;border:1px solid var(--line);margin-right:2px;vertical-align:middle}
  /* envelopes */
  .env-front .brand{position:absolute;left:14px;top:14px}
</style>
</head>
<body>

<!-- business cards -->
<div class="caption" style="left:15px;top:8px;width:95px">Business Card (Front)</div>
<div class="sheet card card-front" style="left:15px">
  <div class="brand"><span class="brand-dot" style="width:8px;height:8px"></span>
    <div><div class="brand-name">Marla Quenby &amp; Associates</div></div></div>
  <div class="card-contact">Marla Quenby<br>PO Box 382 Northville, MI 48193<br>marlaequenby@postvane.com</div>
  <svg class="wave" viewBox="0 0 95 12" height="12" preserveAspectRatio="none"><path d="M0 6 Q45 0 95 4 V12 H0Z" fill="var(--blue)"/><path d="M0 10 Q45 4 95 7 V12 H0Z" fill="var(--brown)"/></svg>
</div>
<div class="caption" style="left:118px;top:8px;width:95px">Business Card (Back)</div>
<div class="sheet card" style="left:118px">
  <div class="brand" style="position:absolute;left:10px;top:20px"><span class="brand-dot" style="width:8px;height:8px"></span><div class="brand-name">Marla Quenby &amp; Associates</div></div>
  <svg class="wave" viewBox="0 0 95 12" height="12" preserveAspectRatio="none"><path d="M0 6 Q45 0 95 4 V12 H0Z" fill="var(--blue)"/><path d="M0 10 Q45 4 95 7 V12 H0Z" fill="var(--brown)"/></svg>
</div>
<div class="caption" style="left:221px;top:8px;width:95px">Business Card (Back)</div>
<div class="sheet card card-back card-blue" style="left:221px">
  <div class="brand"><span class="brand-dot" style="width:8px;height:8px;background:#fff"></span><div class="brand-name">Marla Quenby &amp; Associates</div></div>
</div>
<div class="caption" style="left:324px;top:8px;width:95px">Business Card (Back)</div>
<div class="sheet card card-back card-brown" style="left:324px">
  <div class="brand"><span class="brand-dot" style="width:8px;height:8px;background:#fff"></span><div class="brand-name">Marla Quenby &amp; Associates</div></div>
</div>

<!-- fax cover -->
<div class="caption" style="left:15px;top:98px;width:380px">Fax Cover</div>
<div class="sheet" style="left:15px;top:105px;width:380px;height:555px">
  <div class="pattern" role="img" aria-label="faint decorative pattern of scattered squares" style="left:40px;top:90px;width:320px;height:360px"></div>
  <div class="brand" style="position:absolute;left:18px;top:18px"><span class="brand-dot" style="width:20px;height:20px"></span>
    <div><div class="brand-name" style="font-size:13px">Marla Quenby &amp; Associates</div><div class="brand-tag">BACKGROUND SCREENING &amp; COMPLIANCE CONSULTING</div></div></div>
  <div class="fax-title">FAX</div>
  <table class="fax-table" style="width:344px">
    <tr><td class="lbl">To:</td><td></td><td class="lbl">From:</td><td></td></tr>
    <tr><td class="lbl">Fax:</td><td></td><td class="lbl">Pages:</td><td></td></tr>
    <tr><td class="lbl">Phone:</td><td></td><td class="lbl">Date:</td><td></td></tr>
    <tr><td class="lbl">Re:</td><td></td><td class="lbl">CC:</td><td></td></tr>
  </table>
  <div class="fax-checks"><span>Urgent</span><span>For Review</span><span>Please Comment</span><span>Please Reply</span><span>Please Recycle</span></div>
  <svg class="wave" viewBox="0 0 380 28" height="28" preserveAspectRatio="none"><path d="M0 10 Q180 -4 380 8 V28 H0Z" fill="var(--blue)"/><path d="M0 8 Q180 -2 380 6 L380 9 Q180 1 0 12Z" fill="var(--brown)"/></svg>
  <div class="footer-text">PO Box 382 Northville, MI 48193 &nbsp;|&nbsp; (248) 555-0142 &nbsp;|&nbsp; marlaequenby@postvane.com</div>
</div>

<!-- letterhead -->
<div class="caption" style="left:402px;top:98px;width:380px">Letter Head</div>
<div class="sheet" style="left:402px;top:105px;width:380px;height:555px">
  <div class="pattern" role="img" aria-label="faint decorative pattern of scattered squares" style="left:40px;top:90px;width:320px;height:360px"></div>
  <div class="brand" style="position:absolute;left:18px;top:18px"><span class="brand-dot" style="width:20px;height:20px"></span>
    <div><div class="brand-name" style="font-size:13px">Marla Quenby &amp; Associates</div><div class="brand-tag">BACKGROUND SCREENING &amp; COMPLIANCE CONSULTING</div></div></div>
  <svg class="wave" viewBox="0 0 380 28" height="28" preserveAspectRatio="none"><path d="M0 10 Q180 -4 380 8 V28 H0Z" fill="var(--blue)"/><path d="M0 8 Q180 -2 380 6 L380 9 Q180 1 0 12Z" fill="var(--brown)"/></svg>
  <div class="footer-text">PO Box 382 Northville, MI 48193 &nbsp;|&nbsp; (248) 555-0142 &nbsp;|&nbsp; marlaequenby@postvane.com</div>
</div>

<!-- envelope front -->
<div class="caption" style="left:810px;top:40px;width:380px">Envelope (Front)</div>
<div class="sheet env-front" style="left:810px;top:48px;width:380px;height:185px">
  <div class="pattern" role="img" aria-label="faint decorative pattern of scattered squares" style="left:120px;top:20px;width:180px;height:140px"></div>
  <div class="brand"><span class="brand-dot" style="width:16px;height:16px"></span>
    <div><div class="brand-name" style="font-size:10px">Marla Quenby &amp; Associates</div><div class="brand-tag">PO Box 382 Northville, MI 48193</div></div></div>
  <svg class="wave" viewBox="0 0 380 26" height="26" preserveAspectRatio="none"><path d="M0 10 Q180 -4 380 8 V26 H0Z" fill="var(--blue)"/><path d="M0 8 Q180 -2 380 6 L380 9 Q180 1 0 12Z" fill="var(--brown)"/></svg>
</div>

<!-- envelope backs -->
<div class="caption" style="left:880px;top:340px;width:310px">Envelope (Back)</div>
<svg class="sheet" style="left:880px;top:350px;width:310px;height:75px" viewBox="0 0 310 75">
  <rect width="310" height="75" fill="var(--paper)"/>
  <path d="M0 0 L155 38 L310 0" fill="none" stroke="var(--line)" stroke-width=".8"/>
  <path d="M0 75 L130 40 M310 75 L180 40" stroke="var(--line)" stroke-width=".6"/>
  <circle cx="155" cy="24" r="7" fill="var(--blue)"/>
</svg>
<div class="caption" style="left:880px;top:428px;width:310px">Envelope (Back)</div>
<svg class="sheet" style="left:880px;top:436px;width:310px;height:75px" viewBox="0 0 310 75">
  <rect width="310" height="75" fill="var(--paper)"/>
  <path d="M0 0 H310 V20 L155 38 L0 20Z" fill="var(--blue)"/>
  <path d="M0 20 L155 38 L310 20" fill="none" stroke="var(--navy)" stroke-width="1"/>
  <path d="M0 75 L130 42 M310 75 L180 42" stroke="var(--line)" stroke-width=".6"/>
</svg>
<div class="caption" style="left:880px;top:514px;width:310px">Envelope (Back)</div>
<svg class="sheet" style="left:880px;top:522px;width:310px;height:75px" viewBox="0 0 310 75">
  <rect width="310" height="75" fill="var(--paper)"/>
  <path d="M0 0 H310 V20 L155 38 L0 20Z" fill="var(--brown)"/>
  <path d="M0 20 L155 38 L310 20" fill="none" stroke="var(--brown-light)" stroke-width="1"/>
  <path d="M0 75 L130 42 M310 75 L180 42" stroke="var(--line)" stroke-width=".6"/>
</svg>

</body>
</html>
```